2 Business Card Designs

Need two business cards designed:
1) for lumora films (wedding video) website is lumorafilms.com.au
2) for lumora films (corporate video) website is lumorafilms.net.au

I am looking for something simple, no fancy shapes etc. Just elegant, simple and classy.

Both companies are video companies, one specialising in weddings the other corporate videos. Neither card needs to have any pics of video or camera related images. Please use same colour schemes as respective websites.

Logo is the same but can change colour.

Industry/Entity Type

Camera

Requirements
Must have
• Logo should be either all white or a colour to match websites
Should not have
• swirls, flowers, shapes, etc.

```html
<!DOCTYPE html>
<html lang="en">
<head>
<meta charset="utf-8">
<title>Lumora Films business cards</title>
<link rel="stylesheet" href="https://fonts.googleapis.com/css2?family=Questrial&family=Arimo:wght@700&display=swap">
<style>
  :root {
    --page: #ffffff;
    --card: #e4e8ea;
    --card-edge: #d6dcdf;
    --ink-dark: #1f2424;
    --ink-green: #5d6a51;
    --band-dark: #1d2221;
    --band-green: #5b6a4f;
    --band-text: #f2f2f2;
    --detail: #1a1a1a;
  }
  * { box-sizing: border-box; margin: 0; padding: 0; }
  html, body {
    width: 1200px; height: 698px; overflow: hidden;
    background: var(--page);
  }
  .sheet {
    position: relative; width: 1200px; height: 698px;
    display: grid;
    grid-template-columns: 584px 584px;
    grid-template-rows: 333px 333px;
    column-gap: 11px; row-gap: 11px;
    padding: 12px;
  }
  .card {
    position: relative; overflow: hidden;
    border-radius: 20px;
    background: var(--card);
    font-family: "Questrial", sans-serif;
  }
  .card__texture {
    position: absolute; inset: 0;
    background: linear-gradient(180deg, #e8ecee 0%, var(--card) 55%, var(--card-edge) 100%);
  }
  .wordmark {
    position: absolute; left: 0; right: 0;
    text-align: center; font-weight: 400;
    letter-spacing: 1px; line-height: 1;
  }
  .wordmark--front { top: 100px; font-size: 64px; }
  .wordmark--back { top: 120px; font-size: 46px; }
  .card--corporate .wordmark { color: var(--ink-dark); }
  .card--wedding .wordmark { color: var(--ink-green); }
  .contact {
    position: absolute; left: 0; right: 0; top: 214px;
    display: flex; justify-content: center; gap: 14px;
    font-family: "Arimo", sans-serif; font-weight: 700;
    font-size: 11px; color: var(--detail);
  }
  .contact__sep { font-weight: 400; }
  .band {
    position: absolute; left: 0; right: 0; bottom: 0; height: 50px;
    display: flex; align-items: center; justify-content: center;
    color: var(--band-text); font-size: 19px; letter-spacing: 1px;
  }
  .card--corporate .band { background: var(--band-dark); }
  .card--wedding .band { background: var(--band-green); }
  .band__sep {
    display: inline-block; width: 1px; height: 12px;
    background: var(--band-text); margin: 0 12px; opacity: .8;
  }
  .band--url { font-size: 21px; }
</style>
</head>
<body>
<main class="sheet">
  <section class="card card--corporate card--front">
    <div class="card__texture" role="img" aria-label="Faint repeated light grey lettering texture across the card"></div>
    <p class="wordmark wordmark--front">lumora films</p>
    <div class="band">corporate<span class="band__sep"></span>events<span class="band__sep"></span>multimedia</div>
  </section>

  <section class="card card--corporate card--back">
    <div class="card__texture" role="img" aria-label="Faint repeated light grey lettering texture across the card"></div>
    <p class="wordmark wordmark--back">lumora films</p>
    <p class="contact">
      <span>Name : Mara Ellis</span><span class="contact__sep">|</span>
      <span>Email : info@lumorafilms.com.au</span><span class="contact__sep">|</span>
      <span>Phone : 987 654 3210</span>
    </p>
    <div class="band band--url">www.lumorafilms.net.au</div>
  </section>

  <section class="card card--wedding card--front">
    <div class="card__texture" role="img" aria-label="Faint repeated light grey lettering texture across the card"></div>
    <p class="wordmark wordmark--front">lumora films</p>
    <div class="band">weddings<span class="band__sep"></span>events<span class="band__sep"></span>corporate</div>
  </section>

  <section class="card card--wedding card--back">
    <div class="card__texture" role="img" aria-label="Faint repeated light grey lettering texture across the card"></div>
    <p class="wordmark wordmark--back">lumora films</p>
    <p class="contact">
      <span>Name : Mara Ellis</span><span class="contact__sep">|</span>
      <span>Email : info@lumorafilms.com.au</span><span class="contact__sep">|</span>
      <span>Phone : 987 654 3210</span>
    </p>
    <div class="band band--url">www.lumorafilms.com.au</div>
  </section>
</main>
</body>
</html>
```